Hip Music Management Co. BIz Card

I have a logo (attached) the back side of the card should the full logo on the entire card- that's it. The front side of the card should show the logo somewhere, keeping with the 4 different shades of blue. The front side of the card can be a white background with logo and colored typeface for all info. Pretty simple.

Target Market(s)

I manage and produce a whole bunch of major label and indie artists.

Industry/Entity Type

Management

Contact Information for Business Card

Velmora Sound House (logo)
Dale Fornwick
President
www.velmorasoundhouse.com
dale@velmorasoundhouse.com
+1 310.555.7182
418 Willow Bend Lane
Ashgrove Falls, NY 10599

Requirements
Must have
• Entire logo on back side. White background on front- unless you provide something more interesting.
Nice to have
• On the front of the card if you choose a white backgound, if possible take my logo without the blue background (over white) that would be cool.

```html
<!DOCTYPE html>
<html lang="en">
<head>
<meta charset="utf-8">
<title>Velmora Sound House – Business Card</title>
<link rel="stylesheet" href="https://fonts.googleapis.com/css2?family=Cabin:wght@400;600;700&display=swap">
<style>
  :root {
    --stage: #a6a6a4;
    --navy: #1a1c4b;
    --navy-back: #171d4b;
    --cyan: #2bb5cf;
    --sky: #2f9fdc;
    --ink: #232657;
    --white: #ffffff;
  }
  * { box-sizing: border-box; margin: 0; padding: 0; }
  html, body {
    width: 1200px; height: 1000px; overflow: hidden;
    background: var(--stage);
    font-family: "Cabin", "Gill Sans", sans-serif;
  }
  .canvas { position: relative; width: 1200px; height: 1000px; }

  .card { position: absolute; overflow: hidden; }

  .card-back {
    left: 510px; top: 100px; width: 593px; height: 346px;
    background: var(--navy-back);
    display: flex; align-items: center; justify-content: center;
  }
  .card-back .wordmark {
    color: var(--cyan);
    font-weight: 700;
    font-size: 38px;
    letter-spacing: 1px;
    text-transform: uppercase;
    margin-top: -26px;
  }

  .card-front {
    left: 100px; top: 332px; width: 600px; height: 352px;
    background: var(--white);
  }
  .card-front .wave { position: absolute; left: 0; top: 0; width: 600px; height: 352px; }
  .card-front .wordmark {
    position: absolute; left: 28px; top: 24px;
    color: var(--cyan);
    font-weight: 700;
    font-size: 19px;
    letter-spacing: 0.5px;
    text-transform: uppercase;
  }
  .identity {
    position: absolute; left: 0; right: 0; top: 90px;
    text-align: center; color: var(--ink);
  }
  .identity .name { font-size: 27px; font-weight: 400; letter-spacing: 0.5px; text-transform: uppercase; }
  .identity .title { font-size: 19px; margin-top: 2px; }

  .contacts {
    position: absolute; left: 30px; top: 208px;
    list-style: none; color: var(--white);
  }
  .contacts li {
    display: flex; align-items: center;
    height: 30px; font-size: 20px; letter-spacing: 0.2px;
  }
  .contacts svg { width: 20px; height: 22px; margin-right: 18px; flex: none; }
</style>
</head>
<body>
<main class="canvas">

  <section class="card card-back" aria-label="Card back">
    <p class="wordmark">Velmora Sound House</p>
  </section>

  <section class="card card-front" aria-label="Card front">
    <svg class="wave" viewBox="0 0 600 352" aria-hidden="true">
      <path d="M0 123 Q300 240 600 164 L600 352 L0 352 Z" fill="var(--navy)"/>
    </svg>

    <p class="wordmark">Velmora Sound House</p>

    <div class="identity">
      <p class="name">Dale Fornwick</p>
      <p class="title">President</p>
    </div>

    <ul class="contacts">
      <li>
        <svg viewBox="0 0 20 22" aria-hidden="true" fill="none" stroke="var(--sky)" stroke-width="2">
          <rect x="5" y="1" width="10" height="20" rx="1.5"/>
          <line x1="5" y1="16" x2="15" y2="16"/>
        </svg>
        +1 310.555.7182
      </li>
      <li>
        <svg viewBox="0 0 20 22" aria-hidden="true" fill="none" stroke="var(--sky)" stroke-width="1.8">
          <path d="M2 9 L10 3 L18 9 V19 H2 Z"/>
          <path d="M2 9 L10 15 L18 9"/>
          <path d="M2 19 L8 13 M18 19 L12 13"/>
        </svg>
        dale@velmorasoundhouse.com
      </li>
      <li>
        <svg viewBox="0 0 20 22" aria-hidden="true" fill="none" stroke="var(--sky)" stroke-width="1.8">
          <rect x="3" y="4" width="14" height="10"/>
          <path d="M1 18 H19 L17 14 H3 Z"/>
        </svg>
        www.velmorasoundhouse.com
      </li>
      <li>
        <svg viewBox="0 0 20 22" aria-hidden="true">
          <path d="M10 1 C5.5 1 3 4.3 3 8 C3 13 10 21 10 21 C10 21 17 13 17 8 C17 4.3 14.5 1 10 1 Z" fill="var(--sky)"/>
          <circle cx="10" cy="8" r="2.6" fill="var(--navy)"/>
        </svg>
        418 Willow Bend Lane Ashgrove Falls, NY 10599
      </li>
    </ul>
  </section>

</main>
</body>
</html>
```